IT services web page design

Hello!

We need new design for our web site, obviously :)

Our company is service oriented and we are maintaining, configuring and fixing problems for IT + selling other internet related services.

Our speciality are in area of internet services (web, dns, email, databases, backup...) and internet servers technology.

We also provide service and sales of Zentor Apps and Halvorix Quorvo365 for which we are certified by Zentor and Halvorix.

Other services that we provide (not so in focus) are: VPS hosting, remote backup, web hosting, vexalink fixing...

People mostly call us when they have a problems and this is core idea that new web site has to communicate - We can fix your server / web / email problems, save your money and as* :)

Our team have 15+ years experience with all range of internet technology + bunch of certificates from Halvorix and Tandix [we need to show people we have certificates].
Our qualities: experience, knowledge, delivery on time

In start we will not have blog section, but we need it in future. We also need place for plonkit feeds on web site.

Depth of the site should be max. level 2.

This site will go out in two languages so we need switch button on page from pone language to another.

Target Market(s)

small and mid size business that use internet services for daily operations and main business

Industry/Entity Type

Internet

Requirements
Must have
• * design should be in the way that responsive web could be made

Nice to have
• Long format will be OK for us. Like today pages that list all services and benefits on one loooong web page...

Logo is in attachment. It will be nice to have it on web site but if you find it not appropriate you can change it or put another one.

```html
<!DOCTYPE html>
<html lang="en">
<head>
<meta charset="utf-8">
<title>Velmora Groupa IT Solutions</title>
<link href="https://fonts.googleapis.com/css2?family=Open+Sans:ital,wght@0,400;0,600;0,700;1,700&family=Arimo:wght@400;700&display=swap" rel="stylesheet">
<style>
:root{
  --blue:#1a5fc4;
  --blue-dark:#0d3f97;
  --navy:#0a3d95;
  --navy-deep:#062a5c;
  --green:#3f9b16;
  --green-light:#6cc22a;
  --lime:#b8e034;
  --ink:#222;
  --text:#555;
  --title:#0d3b6e;
  --line:#d6d6d6;
  --page:#f4f5f6;
}
*{box-sizing:border-box;margin:0;padding:0}
html,body{width:989px;height:1200px;overflow:hidden}
body{position:relative;background:var(--page);font-family:"Arimo",Arial,sans-serif;color:var(--text);font-size:10px}
.abs{position:absolute}
.topline{left:0;top:0;width:989px;height:2px;background:#666}
.lang{left:692px;top:0;width:137px;height:24px;background:#333;border-radius:0 0 16px 16px;color:#fff;font-size:10px;display:flex;align-items:center;justify-content:center;gap:6px}
.lang .flag{width:16px;height:10px;background:#c8102e;border:1px solid #fff}
.brand{left:146px;top:30px;display:flex;align-items:center;gap:8px;font-family:"Open Sans",sans-serif;font-weight:700;font-size:24px;color:#111}
.brand .dot{width:40px;height:40px;border-radius:50%;background:#2f7fc4}
.callus{left:705px;top:30px;font-size:10px;color:#222;white-space:nowrap}
.callus b{font-size:13px;font-weight:400}
.hbtn{top:54px;height:24px;border-radius:3px;color:#fff;font-size:10px;display:flex;align-items:center;gap:5px;padding:0 7px;white-space:nowrap}
.hbtn.remote{left:655px;width:100px;background:linear-gradient(#2f6fd0,#184ea9)}
.hbtn.support{left:765px;width:64px;background:linear-gradient(#53b61f,#2f8a0d)}
.nav{left:0;top:99px;width:989px;height:32px;background:linear-gradient(#2a6fd3,#174fb0)}
.nav a{position:absolute;top:0;height:32px;line-height:31px;color:#fff;font-family:"Open Sans",sans-serif;font-size:13px;text-decoration:none;text-align:center;border-right:1px solid #1a4796}
.nav a.on{background:linear-gradient(#63b82a,#3f9115)}
.search{left:675px;top:104px;width:155px;height:22px;background:#fff;border-radius:2px;font-size:10px;color:#666;padding:5px 8px}
.panel{left:146px;top:131px;width:697px;height:901px;background:#fff;box-shadow:0 0 6px rgba(0,0,0,.15)}
.hero{left:158px;top:143px;width:671px;height:279px;background:linear-gradient(100deg,#9ea6ae 0%,#d9dde1 40%,#eef1f4 70%,#f7f8fa 100%)}
.hero h1{position:absolute;left:350px;top:80px;font-family:"Open Sans",sans-serif;font-weight:700;font-size:20px;letter-spacing:-.3px;color:var(--title);white-space:nowrap}
.hero .sub{position:absolute;left:359px;top:112px;width:240px;font-family:"Open Sans",sans-serif;font-weight:600;font-size:12.5px;color:#222;line-height:20px}
.hero .lead{position:absolute;left:359px;top:156px;width:310px;font-family:"Open Sans",sans-serif;font-size:10.5px;color:#222;line-height:16px}
.hero .more{position:absolute;left:357px;top:195px;width:112px;height:26px;border-radius:14px;background:linear-gradient(#5cc020,#2d8a08);color:#fff;font-family:Georgia,serif;font-weight:700;font-size:12px;display:flex;align-items:center;gap:10px;padding-left:8px;border:2px solid #8fd95a}
.hero .more i{width:12px;height:12px;border-radius:50%;background:#fff;position:relative}
.hero .more i:after{content:"";position:absolute;left:4px;top:3px;border-left:5px solid var(--green);border-top:3px solid transparent;border-bottom:3px solid transparent}
.dots{position:absolute;left:601px;top:259px;display:flex;gap:4px}
.dots span{width:11px;height:11px;border-radius:50%;background:#eee;box-shadow:0 1px 2px #999}
.dots span.on{background:var(--blue)}
.arrow{top:269px;width:28px;height:28px;border-radius:50%;background:#fff;border:1px solid #bbb;font-size:16px;color:#444;text-align:center;line-height:25px}
.card{top:443px;width:215px;height:99px;border:1px solid var(--line);background:#fff;box-shadow:0 2px 3px rgba(0,0,0,.1)}
.card h3{height:27px;background:linear-gradient(#2a8ae0,#1158b8);color:#fff;font-family:"Open Sans",sans-serif;font-weight:400;font-size:15px;padding:2px 12px;position:relative}
.card h3:after{content:"";position:absolute;right:6px;top:3px;width:21px;height:21px;border-radius:50%;background:rgba(255,255,255,.3)}
.card p{position:absolute;left:11px;top:37px;width:150px;line-height:12.5px;font-size:9px}
.card .pic{position:absolute;right:10px;top:35px;width:48px;height:50px;border-radius:6px}
.card a{position:absolute;left:13px;top:83px;font-size:9px;font-weight:700;color:#333;text-decoration:none}
.welcome h2{position:absolute;left:0;top:0;font-family:"Open Sans",sans-serif;font-weight:400;font-size:16px;color:#111;display:flex;align-items:center;gap:6px;white-space:nowrap}
.welcome h2 span{color:var(--blue)}
.welcome h2 i{width:22px;height:22px;border-radius:50%;background:#1d5c86;display:block}
.welcome{left:158px;top:563px;width:441px}
.welcome hr{position:absolute;left:0;top:26px;width:432px;border:0;border-top:1px dashed #999}
.welcome p{position:absolute;left:0;top:35px;width:441px;text-align:justify;font-size:9.3px;line-height:13.4px}
.btn-green{background:linear-gradient(#54b41e,#2f8a0d);color:#fff;border-radius:2px;font-size:10px;display:flex;align-items:center;justify-content:center;white-space:nowrap}
.tweet{left:615px;top:561px;width:215px;height:150px;border:1px solid var(--line);background:#fff;box-shadow:0 2px 3px rgba(0,0,0,.1)}
.tweet h3{height:26px;background:linear-gradient(#6cc22a,#3f9b16);color:#fff;font-family:"Open Sans",sans-serif;font-weight:400;font-size:15px;padding:2px 36px;position:relative}
.tweet h3:before{content:"";position:absolute;left:10px;top:6px;width:16px;height:13px;background:#fff;border-radius:3px}
.tweet h3:after{content:"";position:absolute;right:6px;top:3px;width:20px;height:20px;border-radius:50%;background:rgba(255,255,255,.3)}
.tweet .thumb{position:absolute;left:8px;top:32px;width:62px;height:60px;border:1px solid #ccc;background:#fff;padding:6px;font-family:"Open Sans",sans-serif;font-weight:700;font-size:10px;color:#222;line-height:12px}
.tweet h4{position:absolute;left:80px;top:32px;font-size:11px;color:var(--blue);font-weight:700;white-space:nowrap}
.tweet .date{position:absolute;left:80px;top:50px;font-size:8.5px;color:#222;white-space:nowrap}
.tweet p{position:absolute;left:80px;top:66px;width:128px;font-size:8.5px;line-height:11.2px;color:#222}
.tweet a{position:absolute;right:13px;top:128px;font-size:9px;font-weight:700;color:#333;text-decoration:none}
.feature{top:738px;width:150px;height:60px}
.feature .ic{position:absolute;left:0;top:0;width:50px;height:50px;border-radius:50%;background:#eee}
.feature .ic i{position:absolute;left:10px;top:10px;width:30px;height:30px;border-radius:50%;display:block}
.feature h4{position:absolute;left:57px;top:1px;font-size:11.5px;color:#333;white-space:nowrap}
.feature p{position:absolute;left:57px;top:18px;width:92px;font-size:9px;line-height:12.5px}
.saying{left:158px;top:808px;width:671px;height:26px;display:flex;align-items:center;gap:8px}
.saying span.l{flex:1;height:2px;background:linear-gradient(90deg,transparent,var(--blue-dark))}
.saying span.r{flex:1;height:2px;background:linear-gradient(90deg,var(--blue-dark),transparent)}
.saying h2{font-family:"Open Sans",sans-serif;font-style:italic;font-weight:700;font-size:19px;color:#145aa8;white-space:nowrap}
.quote{top:848px;width:327px;height:91px;border:1px solid var(--line);background:#fff;box-shadow:0 2px 3px rgba(0,0,0,.1)}
.quote .mark{position:absolute;left:6px;top:-6px;font-family:Georgia,serif;font-size:60px;color:#ddd}
.quote p{position:absolute;left:18px;top:21px;width:300px;font-size:9px;line-height:13px;color:#444}
.quote .who{position:absolute;right:10px;top:64px;text-align:right;font-size:9px;line-height:12px;color:#444}
.quote .who b{color:#333}
.contact{left:160px;top:968px;width:670px;height:31px;background:#f0f0f0;border:1px solid #ddd}
.contact .tag{position:absolute;left:0;top:0;width:90px;height:31px;background:linear-gradient(#2a8ae0,#1158b8);color:#fff;font-family:"Open Sans",sans-serif;font-size:12.5px;display:flex;align-items:center;padding-left:22px;clip-path:polygon(0 0,82% 0,100% 50%,82% 100%,0 100%);white-space:nowrap}
.contact .tag:before{content:"";position:absolute;left:5px;top:11px;width:12px;height:9px;border:1px solid #fff}
.field{position:absolute;top:6px;height:17px;background:#fff;border:1px solid #ccc;font-size:8.5px;color:#aaa;padding:3px 5px;white-space:nowrap}
.footer{left:0;top:1032px;width:989px;height:137px;background:var(--navy)}
.footer h5{position:absolute;top:13px;font-family:"Open Sans",sans-serif;font-weight:400;font-size:13px;color:var(--lime);border-bottom:1px solid #6c8ccc;padding-bottom:1px;white-space:nowrap}
.footer ul{position:absolute;left:159px;top:42px;list-style:none;color:#fff;font-size:9px;line-height:17px}
.footer .ftext{position:absolute;color:#fff;font-size:9px;line-height:12px}
.footer .rows{position:absolute;left:283px;top:70px;font-size:9px;color:#fff;line-height:15.5px;white-space:nowrap}
.footer .rows b{color:var(--lime);font-weight:400;display:inline-block;width:40px}
.socials{position:absolute;left:680px;top:41px;display:flex;gap:9px}
.socials span{width:22px;height:22px;border-radius:3px;background:#5a7fc9}
.fbrand{position:absolute;left:683px;top:77px;display:flex;align-items:center;gap:6px;font-family:"Open Sans",sans-serif;font-weight:700;font-size:19px;color:#fff;white-space:nowrap}
.fbrand i{width:40px;height:40px;border-radius:50%;background:#6f93d4;display:block}
.bottom{left:0;top:1169px;width:989px;height:31px;background:var(--navy-deep);color:#fff;font-size:9px;padding:10px 0 0 158px}
</style>
</head>
<body>
<div class="abs topline"></div>
<div class="abs lang">Language: ▾ <span class="flag"></span></div>
<div class="abs brand">Velmora grupa <span class="dot"></span></div>
<div class="abs callus">Call Us <b>555.014.2290</b></div>
<div class="abs hbtn remote">
  <svg width="14" height="12" viewBox="0 0 14 12"><rect x="1" y="1" width="12" height="8" fill="none" stroke="#fff"/><path d="M4 11h6" stroke="#fff"/></svg>Remote Access</div>
<div class="abs hbtn support">
  <svg width="14" height="12" viewBox="0 0 14 12"><path d="M2 9V6a5 5 0 0 1 10 0v3" fill="none" stroke="#fff" stroke-width="1.5"/></svg>Support</div>

<nav class="abs nav">
  <a class="on" style="left:159px;width:73px">Home</a>
  <a style="left:232px;width:130px">Our Company</a>
  <a style="left:362px;width:100px">Services</a>
  <a style="left:462px;width:116px">Technology</a>
  <a style="left:578px;width:92px;border:0">Support</a>
</nav>
<div class="abs search">Search</div>

<div class="abs panel"></div>

<section class="abs hero" role="img" aria-label="Business people standing on a grey world map with network lines">
  <h1>Velmora Groupa IT Solutions</h1>
  <div class="sub">We can fix your server | web |email problems, save your money</div>
  <div class="lead">Our team have 15+ years experience with all range of internet technology</div>
  <div class="more"><i></i>Read more</div>
  <div class="dots"><span></span><span></span><span class="on"></span><span></span></div>
</section>
<div class="abs arrow" style="left:131px">‹</div>
<div class="abs arrow" style="left:830px">›</div>

<div class="abs card" style="left:158px"><h3>IT Support</h3><p>Lorem ipsum dolor sit amet,consec etuer adipiscing elit, sed di am nonummy..</p><div class="pic" role="img" aria-label="Support agent with headset" style="background:#e8dccd"></div><a>Read more »</a></div>
<div class="abs card" style="left:386px"><h3>IT Solutions</h3><p>Lorem ipsum dolor sit amet,consect etuer adipiscing elit, sed di am nonummy..</p><div class="pic" role="img" aria-label="Orange gears" style="background:linear-gradient(#f6b733,#e08a10);border-radius:50%"></div><a>Read more »</a></div>
<div class="abs card" style="left:614px"><h3>Cloud Services</h3><p>Lorem ipsum dolor sit amet,consec etuer adipiscing elit, sed di am nonummy..</p><div class="pic" role="img" aria-label="Blue cloud" style="background:linear-gradient(#5aa7f0,#1d5fc4);height:30px;top:48px;border-radius:16px"></div><a>Read more »</a></div>

<section class="abs welcome">
  <h2><i></i>Welcome To <span>Velmora Groupa</span></h2>
  <hr>
  <p>Lorem ipsum dolor sit amet, consectetuer adipiscing elit, sed diam nonummy nibh euismod tincidunt ut laoreet dolore magna aliquam erat volutpat. Ut wisi enim ad minim veniam, quis nostrud exerci tation ullamcorper suscipit lobortis nisl ut aliquip ex ea commodo consequat. Duis autem vel eum iriure dolor in hendrerit in vulputate velit esse molestie consequat, vel illum dolore eu feugiat nulla facilisis at vero eros et accumsan et iusto odio dignissim qui blandit praesent luptatum zzril delenit augue duis dolore te feugait nulla facilisi...</p>
</section>
<div class="abs btn-green" style="left:159px;top:688px;width:62px;height:22px">Read More</div>

<aside class="abs tweet">
  <h3>Plonk Feeds</h3>
  <div class="thumb">Velmora grupa</div>
  <h4>Lorem ipsum dolor</h4>
  <div class="date">Published on &nbsp;June 28, 2013</div>
  <p>Lorem ipsum dolor sit amet, consectetuer adipiscing elit, sed diam nonummy euismod tincidunt ut laore olore magna aliquam erat</p>
  <a>Read more »</a>
</aside>

<div class="abs feature" style="left:159px"><div class="ic"><i style="background:#3a7fd6"></i></div><h4>VPS Hosting</h4><p>Lorem ipsum dolor s ita conse cteuer ad ipiscin gelit,</p></div>
<div class="abs feature" style="left:335px"><div class="ic"><i style="background:#e8a33a;border-radius:3px"></i></div><h4>Remote backup</h4><p>Lorem ipsum dolor s ita conse cteuer ad ipiscin gelit,</p></div>
<div class="abs feature" style="left:512px"><div class="ic"><i style="background:#5a9a30"></i></div><h4>Web hosting</h4><p>Lorem ipsum dolor s ita conse cteuer ad ipiscin gelit,</p></div>
<div class="abs feature" style="left:689px"><div class="ic"><i style="background:#2d5d8c"></i></div><h4>Vexalink</h4><p>Lorem ipsum dolor s ita conse cteuer ad ipiscin gelit,</p></div>

<div class="abs saying"><span class="l"></span><h2>What Our Customers are Saying</h2><span class="r"></span></div>

<div class="abs quote" style="left:159px"><span class="mark">“</span><p>Duis aute irure dolor in reprehenderit in voluptate velit esse cillum dolore eu fugiat nulla pariatur. Excepteur sint occaecat cupidatat non proident, sunt in culpa quiExcepteur sint occaecat cupidatat non proident,</p><div class="who"><b>Mr.client name</b><br>Duis aute irure dolor in reprehend</div></div>
<div class="abs quote" style="left:502px"><span class="mark">“</span><p>Duis aute irure dolor in reprehenderit in voluptate velit esse cillum dolore eu fugiat nulla pariatur. Excepteur sint occaecat cupidatat non proident, sunt in culpa quiExcepteur sint occaecat cupidatat non proident,</p><div class="who"><b>Mr.client name</b><br>Duis aute irure dolor in reprehend</div></div>

<form class="abs contact">
  <div class="tag">Contact Us</div>
  <div class="field" style="left:95px;width:85px">First Name</div>
  <div class="field" style="left:186px;width:85px">Last Name</div>
  <div class="field" style="left:276px;width:85px">Phone Number</div>
  <div class="field" style="left:365px;width:85px">Email</div>
  <div class="field" style="left:455px;width:142px">Comments</div>
  <div class="btn-green" style="position:absolute;left:603px;top:6px;width:57px;height:17px;font-weight:700;font-size:9px">Submit</div>
</form>

<footer class="abs footer">
  <h5 style="left:159px;width:76px">Site Map</h5>
  <ul><li>Home</li><li>Our Company</li><li>Services</li><li>Technology</li><li>Contact</li></ul>
  <h5 style="left:283px;width:151px">Contact Us</h5>
  <div class="ftext" style="left:284px;top:42px;width:170px">Lorem ipsum dolor sit amet, consectetuer adipiscing elit, sed diam nonum..</div>
  <div class="rows"><b>Phone :</b>(000) 000-0000<br><b>Email :</b>info@velmora.example<br><b>Fax :</b>(000) 000-0000<br><b>Domain :</b>www.velmora.example</div>
  <h5 style="left:482px">Sign Up Our Newsletter</h5>
  <div class="ftext" style="left:483px;top:42px;width:170px">Lorem ipsum dolor sit amet, consectetuer adipiscing elit, sed diam nonum..</div>
  <div style="position:absolute;left:483px;top:67px;width:151px;height:22px;background:#fff;font-size:8.5px;color:#999;padding:5px 7px">Enter your Email</div>
  <div class="btn-green" style="position:absolute;left:483px;top:98px;width:44px;height:17px">Submit</div>
  <h5 style="left:680px;width:152px">Follow Us</h5>
  <div class="socials"><span></span><span></span><span></span><span></span><span></span></div>
  <div class="fbrand">Velmora grupa <i></i></div>
</footer>
<div class="abs bottom">Velmora grupa IT Solutions &nbsp;Copyright © 2013</div>
</body>
</html>
```